SEO optimized website for Ko-Brava Corporate identity

I need an eye catching website (Flash splash is OK-I think) to help me promote my company of 10 years: Ko-Brava Inc. - we recently just awarded a design win for my logo design. See attached files.

The company name is Ko-Brava Inc. My current website is www.ko-brava-demo.ca and we specialize in large infrastructure - technology integration, both management and engineering. We have worked almost exclusively on VERD projects and wish to promote that.

I need it to be flexible enough for me to add pages for existing case studies and future case studies.

It is difficult to marry technology and green but do your best as I would like to highlight our VERD AP staff members.

The other side of my business is Small Medium Sized Business support and engineering. VOIP, Server, Desktop we have done it all.

My current site is www.ko-brava-demo.ca
Updates

Please use newly attached logo for designs.

All Please see some sample images to incorporate into the deisgns

Reason: Need more time to evaluate

Please use the correct/new logo in all designs

Please use the updated l;og that was included. Thank you.

Reason: I would like designers to modify their deisgns with the actual company logo. Only one design er has gotten it right. Please modify.

Reason: Still no time to devote to this. Sorry

Reason: Not ready to focus on it

Please only use the logo supplied int he source file zip

Target Market(s)

Both large infrstructure facility owners and small and medium sized businesses.

Industry/Entity Type

Business

Requirements
Must have
• SEO optimization
Easy for me to provide content going forward
Link to my FTP site
Links to my main partners
Separate login are for my clients to store files

```html
<!DOCTYPE html>
<html lang="en">
<head>
<meta charset="utf-8">
<title>Ko-Brava Inc. — Technology Solution</title>
<link rel="stylesheet" href="https://fonts.googleapis.com/css2?family=Gelasio:wght@400;700&family=Arimo:wght@400;700&display=swap">
<style>
:root{
  --backdrop:#1b2029;
  --footer-bg:#060709;
  --page:#ffffff;
  --ink:#222222;
  --heading:#1d3448;
  --brand-orange:#e8641e;
  --nav-top:#2a4a5f;
  --nav-bottom:#122636;
  --slider-frame:#1a1f2b;
  --caption:#b9bcc4;
  --card-border:#d6d6d6;
  --band:#d9d9d9;
  --footer-text:#e2e2e2;
}
*{box-sizing:border-box;margin:0;padding:0}
html,body{width:1008px;height:1200px;overflow:hidden}
body{position:relative;background:var(--backdrop);font-family:"Arimo",Arial,sans-serif;color:var(--ink)}
.site-footer-bg{position:absolute;left:0;top:995px;width:1008px;height:205px;background:var(--footer-bg);border-top:1px solid #2b2f36}
.page{position:absolute;left:109px;top:0;width:765px;height:1019px;background:var(--page)}

/* brand */
.brand{position:absolute;left:109px;top:30px;width:765px;display:flex;justify-content:center;align-items:center;gap:12px}
.brand-mark{width:30px;height:30px;background:var(--brand-orange)}
.brand-name{font-family:"Gelasio",Georgia,serif;font-size:42px;line-height:48px;color:var(--heading)}

/* navigation */
.main-nav{position:absolute;left:134px;top:104px;width:713px;height:30px;display:flex;background:linear-gradient(var(--nav-top),var(--nav-bottom));border-top:2px solid #0c1822;border-bottom:3px solid #c9d2d8}
.main-nav a{display:flex;align-items:center;justify-content:center;color:#fff;text-decoration:none;font-family:"Gelasio",Georgia,serif;font-size:13px;border-right:1px solid #5d7686}
.main-nav a:last-child{border-right:none}

/* slider */
.slider{position:absolute;left:134px;top:149px;width:715px;height:319px;background:var(--slider-frame);box-shadow:0 5px 8px rgba(0,0,0,.45)}
.slide-image{position:absolute;left:12px;top:11px;width:690px;height:258px;background:linear-gradient(180deg,#c6ccd2 0%,#aeb4ba 45%,#6d6a60 70%,#3d3a33 100%)}
.slide-arrow{position:absolute;top:116px;width:22px;height:44px;background:#fff}
.slide-arrow.prev{left:12px;border-radius:0 22px 22px 0}
.slide-arrow.next{right:13px;border-radius:22px 0 0 22px}
.slide-arrow svg{position:absolute;top:14px}
.slide-arrow.prev svg{left:3px}
.slide-arrow.next svg{right:3px}
.slide-caption{position:absolute;left:14px;top:274px;width:615px;font-size:11.2px;font-weight:700;line-height:13.5px;color:var(--caption)}

/* content */
.section-title{font-family:"Gelasio",Georgia,serif;font-weight:400;color:var(--heading);font-size:22px}
.intro{position:absolute;left:134px;top:516px;width:336px}
.intro p{font-size:11.3px;line-height:13px;margin-top:10px}
.intro p + p{margin-top:15px}
.services{position:absolute;left:134px;top:726px;width:336px}
.services ul{list-style:none;margin-top:20px}
.services li{font-size:11.3px;line-height:22.4px;padding-left:16px;position:relative}
.services li::before{content:"";position:absolute;left:0;top:9px;width:5px;height:5px;background:#222}

.projects{position:absolute;left:486px;top:516px;width:361px}
.projects .section-title{font-size:19px;text-transform:uppercase}
.project-card{position:absolute;left:0;width:361px;height:122px;border:1px solid var(--card-border);background:linear-gradient(#fff,#eceaea)}
.project-photo{position:absolute;left:11px;top:11px;width:98px;height:97px;border:1px solid #c9c9c9;background:linear-gradient(135deg,#9aa4ae,#3b4148)}
.project-card:nth-of-type(2) .project-photo{background:linear-gradient(135deg,#8fae6a,#4a4e52)}
.project-card:nth-of-type(3) .project-photo{background:linear-gradient(135deg,#d4dade,#3b4048)}
.project-title{position:absolute;left:119px;top:11px;width:150px;font-size:14px;font-weight:400;line-height:17px;color:#222;text-decoration:underline}
.project-text{position:absolute;left:120px;width:225px;font-size:9px;line-height:11.5px;color:#333}

/* partners band */
.partners{position:absolute;left:109px;top:963px;width:765px;height:56px;background:var(--band);display:flex;align-items:center}
.partners h2{font-family:"Gelasio",Georgia,serif;font-size:16.5px;font-weight:700;color:#111;margin-left:31px;padding-right:13px;border-right:1px solid #333;line-height:36px}
.partner-badge{height:26px;margin-left:18px}

/* footer */
.footer-col{position:absolute;top:1036px}
.footer-col h3{font-size:11px;font-weight:400;color:var(--brand-orange);line-height:14px;margin-bottom:7px}
.footer-col li{list-style:none;font-size:11px;line-height:19px;color:var(--footer-text)}
.footer-rule{position:absolute;left:134px;top:1052px;width:499px;height:1px;background:#2c2f35}
.footer-col strong{font-weight:700}
.footer-col a{color:var(--brand-orange)}
.footer-brand{position:absolute;left:682px;top:1092px;display:flex;align-items:center;gap:8px}
.footer-brand .brand-mark{width:30px;height:30px;background:#3a3d42}
.footer-brand span{font-family:"Gelasio",Georgia,serif;font-size:28px;color:#8d9096}
.copyright{position:absolute;right:146px;top:1176px;font-size:9.5px;color:var(--footer-text)}
</style>
</head>
<body>
<div class="site-footer-bg"></div>

<div class="page"></div>

<header class="brand">
  <span class="brand-mark"></span>
  <span class="brand-name">Ko-Brava</span>
</header>

<nav class="main-nav">
  <a href="#" style="width:104px">HOME</a>
  <a href="#" style="width:115px">ABOUT US</a>
  <a href="#" style="width:117px">SERVICES</a>
  <a href="#" style="width:123px">PARTNERS</a>
  <a href="#" style="width:115px">CAREERS</a>
  <a href="#" style="width:139px">CONTACT US</a>
</nav>

<section class="slider">
  <div class="slide-image" role="img" aria-label="Large building structure under construction with a tower crane beside the waterfront"></div>
  <span class="slide-arrow prev"><svg width="10" height="16" viewBox="0 0 10 16"><path d="M8 1 2 8l6 7" fill="none" stroke="#e8641e" stroke-width="1.5"/></svg></span>
  <span class="slide-arrow next"><svg width="10" height="16" viewBox="0 0 10 16"><path d="M2 1l6 7-6 7" fill="none" stroke="#e8641e" stroke-width="1.5"/></svg></span>
  <p class="slide-caption">It is a long established fact that a reader will be distracted by the readable content of a page when looking at its layout.It is a long established fact that a reader will be distracted by the readable content of a page when looking at its layout.</p>
</section>

<section class="intro">
  <h1 class="section-title">Ko-Brava Technology Solution</h1>
  <p>It is a long established fact that a reader will be distracted by the readable content of a page when looking at its layout. The point of using Lorem Ipsum is that it has a more-or-less normal distribution of letters, as opposed to using 'Content here, content here', making it look like readable English. Many desktop publishing packages and web page editors .</p>
  <p>now use Lorem Ipsum as their default model text, and a search for 'lorem ipsum' will uncover many web sites still in their infancy. Various versions have evolved over the years, sometimes by accident, sometimes on purpose (injected humour and the like).</p>
</section>

<section class="services">
  <h2 class="section-title">Main Services</h2>
  <ul>
    <li>Project Management</li>
    <li>IBT</li>
    <li>SMB Support</li>
    <li>Virtualization</li>
    <li>Voice Technologies</li>
    <li>Technology Construction</li>
  </ul>
</section>

<section class="projects">
  <h2 class="section-title">Recent Projects...</h2>
  <article class="project-card" style="top:38px">
    <div class="project-photo" role="img" aria-label="Team meeting around a laptop"></div>
    <h3 class="project-title">Technology Project Management</h3>
    <p class="project-text" style="top:52px">It is a long established fact that a reader will be distracted by the readable content of a page when looking at its layout.l</p>
  </article>
  <article class="project-card" style="top:171px">
    <div class="project-photo" role="img" aria-label="Colleagues discussing work in a bright office"></div>
    <h3 class="project-title" style="width:200px">Services and Support</h3>
    <p class="project-text" style="top:41px">It is a long established fact that a reader will be distracted by the readable content of a page when looking at its layout.ladable content of a page when looking at its layout.l</p>
  </article>
  <article class="project-card" style="top:302px">
    <div class="project-photo" role="img" aria-label="Business team seated around a conference table"></div>
    <h3 class="project-title">Tecnology Space Construction</h3>
    <p class="project-text" style="top:62px">It is a long established fact that a reader will be distracted by the readable content of a page when looking at its layout.l</p>
  </article>
</section>

<section class="partners">
  <h2>Our Partners</h2>
  <span class="partner-badge" style="width:128px;background:#3a3a3a"></span>
  <span class="partner-badge" style="width:92px;background:#4d7fb5;border-radius:13px"></span>
  <span class="partner-badge" style="width:160px;height:30px;background:#2b57a8"></span>
  <span class="partner-badge" style="width:138px;background:#1c1c1c"></span>
</section>

<div class="footer-rule"></div>
<div class="footer-col" style="left:134px"><h3>Services</h3><ul><li>Project Management</li><li>IBT</li><li>SMB Support</li><li>Virtualization</li><li>Voice Technologies</li><li>Technology Construction</li></ul></div>
<div class="footer-col" style="left:291px"><h3>Partners</h3><ul><li>Northline Telecom</li><li>Vocalis</li><li>Lumen AV</li><li>Vector Data</li></ul></div>
<div class="footer-col" style="left:407px"><h3>About</h3><ul><li>Team</li><li>Careers</li><li>Newsroom</li><li>Investors</li><li>Contact</li></ul></div>
<div class="footer-col" style="left:498px"><h3>Ko-Brava</h3><ul><li>48 Ridgeway Court</li><li>Maple Bay, B.C. V0X-1A2</li><li><strong>CANADA</strong></li><li>Tel: 604.555.0148</li><li><a href="#">Email: info@ko-brava-demo.ca</a></li></ul></div>

<div class="footer-brand"><span class="brand-mark"></span><span>Ko-Brava</span></div>
<p class="copyright">Copyright © 2010, Ko-Brava. All rights reserved.</p>
</body>
</html>
```